Attorney Website Design

I need a top quality attorney website layout designed. Here are some examples of what I feel are great websites:
http://www.brelmoradivorceattorney.example/
http://www.vethomirlawfirm.example/
http://www.plexfirm.example/
http://www.harrowgatecriminaldefensefirm.example/
http://www.qzfirm.example/
http://www.tolvermoorcriminaldefensefirm.example/
http://www.drennocriminalattorneys.example/
http://www.qzfirm.example/
What we like about these sites:
• The different layers
• Subtle designs, textures, curves
• 3 dimensional
• Floating effects
• Prominent phone number
• Location of Areas of Practice
• Request A Consultation Prominent
• Right side bar with practice areas
• Badges
• Clear Calls to Action
• Dynamic/Staying Top navigation when you scroll
The project will be for a home page and then also an interior page (should be similar to home page).
I want to make it understood I am looking for a design which is not a typical "template" site which I can find anywhere for $50. This budget and project is for a "Custom" website design. Please submit designs similar in quality to the samples links I have posted. Creativity is a MUST! The best way to explain this is, I want a design that I can feel it unique and original, not something that looks like 95% of all websites out there.
Owen
I just wanted everyone to know that so far I am not to pleased with any of the designs. I am not looking for cut/pasting of other peoples websites but ORIGINAL and CREATIVE work.
Industry/Entity Type
Attorney

```html
<!DOCTYPE html>
<html lang="en">
<head>
<meta charset="utf-8">
<title>Tolvermoor Attorneys</title>
<link href="https://fonts.googleapis.com/css2?family=Open+Sans:wght@300;400;600&family=Lora:ital@1&display=swap" rel="stylesheet">
<style>
:root{
  --red:#c50d0d;
  --ink:#222;
  --text:#7a7a7a;
  --soft:#f3f3f3;
  --line:#d9d9d9;
  --dark:#2b2b2b;
  --white:#fff;
}
*{box-sizing:border-box;margin:0;padding:0}
html,body{width:799px;height:1200px;overflow:hidden}
body{position:relative;background:var(--white);font-family:'Open Sans',sans-serif;color:var(--ink)}
.abs{position:absolute}
ul{list-style:none}

.site-header{left:0;top:0;width:799px;height:62px;background:#f7f7f7;border-bottom:1px solid #ddd}
.brand{left:80px;top:18px;color:var(--red);font-size:22px;font-weight:600;letter-spacing:1px}
.main-nav{right:80px;top:24px;display:flex;font-size:10px}
.main-nav a{color:#444;text-decoration:none;padding:0 9px;border-left:1px solid #ccc;line-height:16px}
.main-nav a:first-child{border-left:0;color:var(--red)}
.main-nav a:last-child{padding-right:0}

.tagline{left:80px;top:74px;width:639px;text-align:center;font-family:'Lora',serif;font-style:italic;font-size:14px;line-height:20px;color:#555}

.hero{left:80px;top:128px;width:639px;height:299px;background:radial-gradient(ellipse at 65% 35%,#e6c9ae 0%,#b88a68 45%,#5a3525 100%)}
.hero-title{left:94px;font-size:27px;color:var(--white);font-weight:400;padding:0 13px;height:36px;line-height:36px}
.hero-title.red{top:208px;background:var(--red)}
.hero-title.black{top:250px;background:#222}
.hero-arrows{left:689px;top:400px;display:flex}
.hero-arrows span{width:11px;height:12px;background:var(--white);border:1px solid #999;display:flex;align-items:center;justify-content:center}
.hero-progress{left:80px;top:427px;width:639px;height:4px;background:#999}
.hero-progress i{display:block;width:195px;height:4px;background:var(--red)}

.about-title{left:80px;top:446px;font-size:21px;font-weight:400}
.about-title em{font-style:normal;color:var(--red)}
.about-text{left:80px;top:481px;width:275px;font-size:8.2px;line-height:13.5px;color:var(--text)}
.link-more{font-size:7px;color:var(--red);text-transform:uppercase;text-decoration:none}
.about .link-more{left:80px;top:535px}
.dots{left:80px;top:555px;display:flex;gap:2px}
.dots i{width:6px;height:6px;border-radius:50%;background:#bbb}
.dots i:last-child{background:var(--white);border:1px solid #bbb}

.office-card{top:453px;width:108px;height:110px;border-top:2px solid var(--red);background:var(--soft);border-bottom:2px solid #ccc}
.office-card .photo{height:84px}
.office-card p{text-align:center;font-size:9.5px;color:var(--red);line-height:22px}

.news-bar{left:80px;top:595px;width:639px;height:25px;background:#eee}
.news-bar .dot{left:8px;top:7px;width:11px;height:11px;border-radius:50%;background:var(--red)}
.news-bar .ticker{left:34px;top:0;line-height:25px;font-size:8.8px;color:#888}
.news-bar .label{right:0;top:0;height:25px;width:106px;background:#2a2a2a;color:var(--white);font-size:14px;font-weight:300;line-height:25px;padding-left:16px;clip-path:polygon(8px 0,100% 0,100% 100%,8px 100%,0 50%)}

.case-photo{left:80px;top:654px;width:206px;height:154px;border-top:2px solid var(--red);background:radial-gradient(ellipse at 35% 45%,#7a2d22 0%,#3b1c16 40%,#c8b9a8 100%)}
.case-caption{left:80px;top:808px;width:206px;height:33px;background:#eee;border-bottom:2px solid #777;text-align:center;line-height:33px;font-size:12px;font-weight:300;color:#777}
.case-body{left:293px;top:651px;width:232px}
.case-body h3{font-size:13.5px;font-weight:400;margin-bottom:4px}
.case-body p{font-size:8.6px;line-height:12px;color:var(--text);margin-bottom:11px}
.case-body p.small{font-size:7.8px}
.case-links{left:295px;top:832px;width:232px;display:flex;justify-content:space-between}

.finder{left:542px;top:654px;width:178px;height:188px;background:#f2f2f2;border:1px solid #ddd}
.finder h4{height:29px;background:var(--red);color:var(--white);font-weight:400;font-size:16px;line-height:29px;padding-left:10px}
.finder p{font-size:7.8px;line-height:12px;color:var(--text);padding:8px 12px 6px}
.finder .field{margin:0 10px 8px 12px;height:20px;background:var(--white);border:1px solid #ddd;font-size:7.5px;color:#aaa;line-height:18px;padding-left:6px}
.finder .btn{margin:3px 0 0 12px;display:inline-block;background:var(--red);color:var(--white);font-size:8.5px;padding:0 6px;line-height:20px}

.divider{left:80px;top:877px;width:639px;height:1px;background:#e5e5e5}

.testimonials-title{left:80px;top:909px;font-size:17px;font-weight:300;color:#333}
.quote-mark{left:80px;top:930px;font-family:'Lora',serif;font-size:34px;color:#ccc}
.testimonial{left:107px;top:950px;width:380px;font-size:8.2px;line-height:12px;color:var(--text)}
.testimonial-name{left:107px;top:1005px;font-size:10px;color:var(--red)}
.v-rule{left:506px;top:916px;width:1px;height:98px;background:#e5e5e5}
.newsletter-title{left:530px;top:925px;font-size:12.5px;color:var(--red)}
.newsletter{left:524px;top:945px;width:196px;height:51px;background:#eee}
.newsletter .lbl{left:13px;top:4px;font-size:7.5px;color:#333}
.newsletter .input{left:9px;top:16px;width:123px;height:17px;background:var(--white)}
.newsletter .join{left:141px;top:16px;width:40px;height:17px;background:#222;color:var(--white);font-size:8.5px;line-height:17px;padding-left:8px;clip-path:polygon(0 0,80% 0,100% 50%,80% 100%,0 100%)}
.newsletter .rss{left:12px;top:38px;font-size:7px;color:var(--red)}

.site-footer{left:0;top:1053px;width:799px;height:147px;background:var(--dark);color:#ddd}
.foot-col{top:23px}
.foot-col h5{font-size:12px;font-weight:400;color:#eee;margin-bottom:13px}
.foot-col li{font-size:8.4px;line-height:14px;color:#ddd}
.foot-col li::before{content:"•";margin-right:4px}
.contact li{display:flex;align-items:center;gap:7px;line-height:19px}
.contact li::before{content:none}
.contact svg{width:9px;height:9px;flex:none}
.foot-rule{left:80px;top:117px;width:639px;height:1px;background:#444}
.copyright{left:81px;top:127px;font-size:8.2px;color:#ccc}
.follow{right:80px;top:125px;display:flex;align-items:center;gap:6px;font-size:8.2px;color:#ccc}
.follow i{width:13px;height:13px;border-radius:50%;background:#eee;display:inline-block}
</style>
</head>
<body>

<header class="site-header abs">
  <div class="brand abs">TOLVERMOOR</div>
  <nav class="main-nav abs">
    <a href="#">Home</a><a href="#">Know your rights</a><a href="#">Check the news</a><a href="#">Read articles</a><a href="#">Contact us</a>
  </nav>
</header>

<p class="tagline abs">Our Law Firm believes that clients' success determines our own. S weensure both by collaborating with our clients to achieve their goals.</p>

<section class="hero abs" role="img" aria-label="Photo of a judge's gavel and brass scales of justice resting on old law books"></section>
<h1 class="hero-title red abs">WALCOME TO</h1>
<h1 class="hero-title black abs">TOLVERMOOR ATTORNEYS</h1>
<div class="hero-arrows abs">
  <span><svg width="6" height="8" viewBox="0 0 6 8"><path d="M5 0L1 4l4 4" fill="none" stroke="#333"/></svg></span>
  <span><svg width="6" height="8" viewBox="0 0 6 8"><path d="M1 0l4 4-4 4" fill="none" stroke="#333"/></svg></span>
</div>
<div class="hero-progress abs"><i></i></div>

<section class="about">
  <h2 class="about-title abs">About <em>Tolvermoor Attorneys</em></h2>
  <p class="about-text abs">There are many variations of passages of Lorem Ipsum available, but the majority have suffered alteration in some form, by injected humour, or randomised words which don't look even slightly believable.</p>
  <a class="link-more abs" href="#">Learn more &nbsp;›</a>
  <div class="dots abs"><i></i><i></i><i></i></div>
</section>

<article class="office-card abs" style="left:369px">
  <div class="photo" role="img" aria-label="Photo of hands signing documents at a desk" style="background:linear-gradient(135deg,#f1e6e6,#9aa0a8 60%,#3a3a3a)"></div>
  <p>Miami Attorneys</p>
</article>
<article class="office-card abs" style="left:490px">
  <div class="photo" role="img" aria-label="Photo of a smiling attorney at an office desk" style="background:linear-gradient(135deg,#b5623f,#d9c7b8 55%,#222)"></div>
  <p>Attorneys in Tampa</p>
</article>
<article class="office-card abs" style="left:611px">
  <div class="photo" role="img" aria-label="Photo of an attorney in a meeting with a statue of justice behind" style="background:linear-gradient(135deg,#e9e4de,#c7bdb1 55%,#2a2a2a)"></div>
  <p>Attorneys Orlando FL</p>
</article>

<div class="news-bar abs">
  <span class="dot abs"></span>
  <span class="ticker abs">The standard chunk of Lorem Ipsum used since the 1500s is reproduced below for those interested. Sections 1.10.32</span>
  <span class="label abs">Latest New's</span>
</div>

<div class="case-photo abs" role="img" aria-label="Close-up photo of a wooden gavel on a desk"></div>
<div class="case-caption abs">Criminal Defense Attorney</div>
<article class="case-body abs">
  <h3>Criminal Defense Attorney</h3>
  <p>Sed ut perspiciatis unde omnis iste natus error sit voluptatem accusantium doloremque laudantium, totam rem aperiam, eaque ipsa quae ab illo inventore veritatis et quasi architecto beatae vitae dicta sunt explicabo.</p>
  <p>Sed ut perspiciatis unde omnis iste natus error sit voluptatem accusantium doloremque laudantium, totam rem aperiam,</p>
  <p class="small">Sed ut perspiciatis unde omnis iste natus error sit voluptatem accusantium doloremque laudantium, totam rem aperiam, laudantium, totam rem aperiam,</p>
</article>
<div class="case-links abs">
  <a class="link-more" href="#">Read more &nbsp;›</a>
  <a class="link-more" href="#" style="margin-top:2px">More case studies &nbsp;›</a>
</div>

<aside class="finder abs">
  <h4>FIND A LAWYER</h4>
  <p>Lorem ipsum dolor sit amet consectetur adipiscing elit, Sed do euismod</p>
  <div class="field">lawyer's name</div>
  <div class="field">law firm name</div>
  <div class="field">law firm name</div>
  <span class="btn">FIND HERE</span>
</aside>

<div class="divider abs"></div>

<h2 class="testimonials-title abs">Client Testimonials</h2>
<span class="quote-mark abs">&ldquo;</span>
<p class="testimonial abs">At vero eos et accusamus et iusto odio dignissimos ducimus qui blanditiis praesentium voluptatum deleniti atque corrupti quos dolores et quas molestias excepturi sint occaecati cupiditate non provident, similique sunt in culpa qui officia deserunt mollitia animi, id est laborum et dolorum fuga. Et harum quidem rerum facilis est et expedita distinctio.</p>
<span class="testimonial-name abs">mara quellin</span>
<div class="v-rule abs"></div>

<h3 class="newsletter-title abs">Newsletter Sign-up</h3>
<div class="newsletter abs">
  <span class="lbl abs">Enter your email address</span>
  <span class="input abs"></span>
  <span class="join abs">JOIN</span>
  <span class="rss abs">Also subscribe to our RSS feed</span>
</div>

<footer class="site-footer abs">
  <div class="foot-col contact abs" style="left:80px;top:23px">
    <h5>Contact Us</h5>
    <ul>
      <li><svg viewBox="0 0 10 10"><path d="M5 0a3.3 3.3 0 0 0-3.3 3.3C1.7 6 5 10 5 10s3.3-4 3.3-6.7A3.3 3.3 0 0 0 5 0zm0 4.6a1.3 1.3 0 1 1 0-2.6 1.3 1.3 0 0 1 0 2.6z" fill="#eee"/></svg>Lorem ipsum dolor sit amet</li>
      <li><svg viewBox="0 0 10 10"><path d="M2 0l2 2.5-1 1.2c.6 1.3 1.6 2.3 2.9 2.9l1.2-1L10 8l-1.5 2C4 10 0 6 0 1.5z" fill="#eee"/></svg>Phone: (+0800).314.962 Fax: 1.804.219</li>
      <li><svg viewBox="0 0 10 10"><path d="M0 2h10v6H0z" fill="#eee"/><path d="M0 2l5 3.5L10 2" fill="none" stroke="#2b2b2b"/></svg>Email : info@lawharbor.example</li>
    </ul>
  </div>
  <div class="foot-col abs" style="left:279px;top:32px"><h5>About Us</h5><ul><li>Lorem ipsum dolor</li><li>Lorem ipsum dolor</li><li>Lorem ipsum dolor</li><li>Lorem ipsum dolor</li></ul></div>
  <div class="foot-col abs" style="left:396px;top:25px"><h5 style="margin-bottom:20px">Services</h5><ul><li>Lorem ipsum dolor</li><li>Lorem ipsum dolor</li><li>Lorem ipsum dolor</li><li>Lorem ipsum dolor</li></ul></div>
  <div class="foot-col abs" style="left:514px;top:25px"><h5 style="margin-bottom:20px">Case Studies</h5><ul><li>Lorem ipsum dolor</li><li>Lorem ipsum dolor</li><li>Lorem ipsum dolor</li><li>Lorem ipsum dolor</li></ul></div>
  <div class="foot-col abs" style="left:638px;top:27px"><h5 style="margin-bottom:18px">Carrers</h5><ul><li>Lorem ipsum dolor</li><li>Lorem ipsum dolor</li><li>Lorem ipsum dolor</li><li>Lorem ipsum dolor</li></ul></div>
  <div class="foot-rule abs"></div>
  <p class="copyright abs">Copy rigthe 2014 © Tolvermoor Attorneys. All rights reserved</p>
  <div class="follow abs">Follow on : &nbsp;<i></i>Friendwall &nbsp;<i></i>Chirper</div>
</footer>

</body>
</html>
```